Web Design Project

Please take a look at my current aged website www.tarlowpeopleadvisory.com and my newly designed logo and business cards. I would like a new fresh updated look to my website and my new designs incorporated.
Updates

  Good Morning Everyone

Due to an Austrralian licencing issue I have had to have my logo slightly redesigned.

Would you please be able to look at the newly uploaded files and revise your designs.

Thanks so much.  I am very happy with the calibre and quality of the designs so far.

kind Regards

Marnie

Industry/Entity Type

Business

Requirements
Must have
• the exisiting pages and fresh new graphics and a real commitment to my palette of lime green, turqouise and black.

```html
<!DOCTYPE html>
<html lang="en">
<head>
<meta charset="utf-8">
<title>Tarlow Consulting</title>
<link href="https://fonts.googleapis.com/css2?family=Arimo:wght@400;700&family=Tinos&display=swap" rel="stylesheet">
<style>
:root{
  --turquoise:#1cafc9;
  --turquoise-dark:#1598b0;
  --lime:#7cc242;
  --lime-dark:#5da82c;
  --black:#000;
  --ink:#444;
  --muted:#666;
  --panel:#eceef1;
  --line:#d5d8dc;
  --white:#fff;
}
*{box-sizing:border-box;margin:0;padding:0}
html,body{width:814px;height:1200px;overflow:hidden;background:var(--white)}
body{position:relative;font-family:"Arimo",Arial,sans-serif;color:var(--ink)}
.abs{position:absolute}

.topbar{left:0;top:0;width:814px;height:54px;background:var(--turquoise);border-bottom:3px solid var(--lime)}
.nav{left:100px;top:0;display:flex;height:51px}
.nav a{color:var(--white);text-decoration:none;font-size:15px;line-height:51px;padding:0 12px}
.nav a.is-active{background:var(--lime);padding:0 12px}
.search{left:590px;top:11px;width:120px;height:26px;border:2px solid var(--black);background:var(--white);display:flex}
.search span{flex:1;font-size:13px;color:var(--turquoise);padding:4px 6px}
.search i{width:30px;background:var(--black);display:flex;align-items:center;justify-content:center}

.hero-band{left:0;top:57px;width:814px;height:348px;background:var(--black)}
.brand{left:107px;top:112px;display:flex;align-items:center;gap:8px;font-size:24px;font-weight:700;color:var(--turquoise)}
.brand b{display:block;width:22px;height:22px;border-radius:50%;background:var(--lime)}

.slider{left:99px;top:162px;width:614px;height:296px;background:var(--lime);border-radius:4px;box-shadow:0 3px 6px rgba(0,0,0,.35)}
.slide{left:7px;top:7px;width:600px;height:262px;background:linear-gradient(135deg,#e9edf1,#c9d3dc 45%,#5f7a9c 75%,#d9dde3)}
.dots{left:0;bottom:4px;width:100%;display:flex;justify-content:center;align-items:center;gap:4px}
.dots .dot{width:13px;height:13px;border-radius:50%;background:#ddd;border:1px solid #999}
.dots .dot.on{background:#222}

.service{top:487px;width:200px;text-align:center}
.service .icon{width:70px;height:70px;margin:0 auto;border-radius:8px}
.service h3{margin-top:16px;font-size:14px;font-weight:700;color:#555}
.btn{display:inline-block;margin-top:14px;background:var(--turquoise);color:var(--white);font-size:10px;width:58px;height:30px;line-height:30px;border-radius:5px}

.consultants{left:100px;top:662px;width:612px;height:215px;border:1px solid #e5e5e5;padding:4px}
.consultants .inner{width:100%;height:100%;background:var(--panel);position:relative}
.consultants h2{left:20px;top:16px;font-size:15px;color:var(--lime-dark);font-weight:700}
.consultants .rule{left:8px;top:38px;width:586px;height:1px;background:var(--line)}
.arrows{left:520px;top:10px;display:flex;gap:8px}
.portrait{left:19px;top:58px;width:140px;height:134px;background:linear-gradient(160deg,#c9cdd1,#6b6257 60%,#2d2a28);border:1px solid #444}
.name{left:174px;top:60px;font-size:11px;font-weight:700;color:#111;text-decoration:underline}
.bio{left:174px;top:83px;width:418px;font-size:9.6px;line-height:17px;color:#555}
.read{left:174px;top:171px;font-size:9.5px;color:#222;background:var(--white);border-radius:4px;padding:4px 6px;box-shadow:0 1px 2px rgba(0,0,0,.15)}

.col-title{top:908px;font-size:13px;font-weight:700;color:#888;text-decoration:underline}
.contact p{font-size:11px;color:var(--lime-dark);margin-bottom:11px}
.contact h4{font-size:13px;color:var(--turquoise);margin-bottom:9px}
.quick a{display:block;font-size:11px;color:var(--turquoise);font-weight:700;text-decoration:none;margin-bottom:16px}
.form{left:539px;top:936px;width:164px;height:195px;background:#e3e3e3;padding:11px 6px}
.form .field{height:14px;background:var(--white);border:1px solid #ccc;border-radius:2px;margin:0 6px 6px;font-size:7px;color:#aaa;padding:2px 4px}
.form label{display:block;font-size:10px;color:#555;margin:6px 2px 3px}
.form .area{height:32px;background:var(--white);border-radius:3px;margin:0 2px}
.submit{display:block;margin:8px auto 0;width:52px;height:18px;background:#444;color:var(--white);font-size:10px;text-align:center;line-height:18px;border-radius:3px}

.footer{left:0;top:1152px;width:814px;height:48px;background:#111;color:#bbb;font-family:"Tinos",serif;font-size:11px;text-align:center;line-height:48px}
</style>
</head>
<body>
<div class="abs topbar"></div>
<nav class="abs nav">
  <a class="is-active">Home</a><a>Our Services</a><a>Our Consultants</a><a>Our Fees</a><a>Contact Us</a>
</nav>
<div class="abs search"><span>Search</span><i><svg width="14" height="14" viewBox="0 0 14 14"><circle cx="6" cy="6" r="4" fill="none" stroke="#7cc242" stroke-width="2"/><line x1="9" y1="9" x2="13" y2="13" stroke="#7cc242" stroke-width="2.4"/></svg></i></div>

<div class="abs hero-band"></div>
<div class="abs brand"><b></b>TarlowConsulting</div>

<div class="abs slider">
  <div class="abs slide" role="img" aria-label="Photo of a smiling consulting team working at computers in a bright office"></div>
  <div class="abs dots">
    <svg width="12" height="14" viewBox="0 0 12 14"><path d="M9 1 3 7l6 6" fill="none" stroke="#fff" stroke-width="3"/></svg>
    <span class="dot"></span><span class="dot on"></span><span class="dot"></span><span class="dot"></span>
    <svg width="12" height="14" viewBox="0 0 12 14"><path d="m3 1 6 6-6 6" fill="none" stroke="#fff" stroke-width="3"/></svg>
  </div>
</div>

<section class="abs service" style="left:91px">
  <div class="icon" role="img" aria-label="Illustration of people above gears" style="background:linear-gradient(#5fc3d3,#7cc242)"></div>
  <h3>People Systems and Processes</h3><span class="btn">Learn More</span>
</section>
<section class="abs service" style="left:320px">
  <div class="icon" role="img" aria-label="Illustration of two figures joining puzzle pieces" style="background:linear-gradient(#d6d6d6,#e6b43a 60%,#3a7fd0)"></div>
  <h3>Employee Relations</h3><span class="btn">Learn More</span>
</section>
<section class="abs service" style="left:531px">
  <div class="icon" role="img" aria-label="Illustration of a computer screen with blocks" style="background:linear-gradient(135deg,#1d8fb0,#3a3f46 60%,#e08a3c)"></div>
  <h3>Organisation Development</h3><span class="btn">Learn More</span>
</section>

<section class="abs consultants">
  <div class="inner">
    <h2 class="abs">Our Consultants</h2>
    <div class="abs arrows">
      <svg width="22" height="22" viewBox="0 0 22 22"><circle cx="11" cy="11" r="9.5" fill="#fff" stroke="#1cafc9" stroke-width="2"/><path d="M13 6 8 11l5 5" fill="none" stroke="#1cafc9" stroke-width="2"/></svg>
      <svg width="22" height="22" viewBox="0 0 22 22"><circle cx="11" cy="11" r="9.5" fill="#fff" stroke="#1cafc9" stroke-width="2"/><path d="m9 6 5 5-5 5" fill="none" stroke="#1cafc9" stroke-width="2"/></svg>
    </div>
    <div class="abs rule"></div>
    <div class="abs portrait" role="img" aria-label="Portrait photo of the principal consultant"></div>
    <div class="abs name">Marnie Tarlow</div>
    <p class="abs bio">With over ten years human resources experience in the mining, allied health, hospitality, manufacturing, asset management and labour hire industries our Principal Consultant Marnie Tarlow is a skilled Human Resources Practitioner. Marnie successfully caters to her client's briefs by providing flexible and collaborative (and cost-efficient) HR solutions. She is able to work in either a remote consultative capacity or in an on-site cohesive team environment.</p>
    <span class="abs read">Read More</span>
  </div>
</section>

<h3 class="abs col-title" style="left:106px">Contact Us:</h3>
<div class="abs contact" style="left:106px;top:944px">
  <p>14 Carrow Lane</p>
  <p>Innaloo&nbsp;&nbsp;WA&nbsp;&nbsp;6099</p>
  <h4>mobile</h4><p>0400 555 217</p>
  <h4>email</h4><p>marnie@tarlowpeopleadvisory.com</p>
  <h4>web</h4><p>www.tarlowpeopleadvisory.com</p>
</div>

<h3 class="abs col-title" style="left:333px">Quick Access:</h3>
<nav class="abs quick" style="left:333px;top:947px">
  <a>Cousultant</a><a>People System &amp; Processes</a><a>Employee Relation</a><a>Organisation Development</a><a>Our Fee</a><a>Our services</a>
</nav>

<h3 class="abs col-title" style="left:539px;font-size:14px">Please fill out the form:</h3>
<form class="abs form">
  <div class="field">First Name:</div>
  <div class="field">Last Name:</div>
  <div class="field">Company:</div>
  <div class="field">Email:</div>
  <div class="field">Phone:</div>
  <label>Comments</label>
  <div class="area"></div>
  <span class="submit">Submit</span>
</form>

<footer class="abs footer">TarlowConsulting©2012 Privacy Policy</footer>
</body>
</html>
```